New Innovative Counselling and psychotherapy Service needs Business Card design

Keep it simple and professional. On one side, just company name and logo (perhaps in all blue) and maybe a tag line.

On other side (all white) my name and Qualifications in centre

Industry/Entity Type

Health And Wellness

Contact Information for Business Card

Derek Hollis
Counsellor & Psychotherapist
BSc (Psychol.), BA, Dip. (Couns. & Psych.), PG.Cert (CBT), ADLnR, ESGW

I will also require Mobile no, Email and web site address of which I'll pass on to final designer.

Font styles to use
Sans Serif

Requirements
Must have
• My Logo Only and please use the colours in logo that is in it.
Should not have
• Any other images

```html
<!DOCTYPE html>
<html lang="en">
<head>
<meta charset="utf-8">
<title>Kindred Lane – Business Card</title>
<link rel="stylesheet" href="https://fonts.googleapis.com/css2?family=Raleway:wght@300;400;600;800&display=swap">
<style>
  :root {
    --brand-blue: #45aee6;
    --brand-blue-deep: #2f95d2;
    --brand-green: #8cc04f;
    --card-white: #f4f4f4;
    --ink-dark: #2a2a2a;
    --divider: #8a8a8a;
    --backdrop: #2c2c2c;
    --text-on-blue: #ffffff;
  }
  * { box-sizing: border-box; margin: 0; padding: 0; }
  html, body {
    width: 1200px;
    height: 997px;
    overflow: hidden;
    background: var(--backdrop);
    font-family: "Raleway", sans-serif;
  }
  .stage {
    position: relative;
    width: 1200px;
    height: 997px;
  }
  .card {
    position: absolute;
    width: 560px;
    height: 320px;
    left: 320px;
    box-shadow: 0 14px 30px rgba(0,0,0,0.45);
  }
  /* Front side */
  .card--front {
    top: 140px;
    background: linear-gradient(135deg, #4ab4ec 0%, var(--brand-blue) 60%, #3ea5dd 100%);
    display: flex;
    align-items: center;
    justify-content: center;
    gap: 22px;
  }
  .brand-dot {
    width: 62px;
    height: 62px;
    border-radius: 50%;
    background: var(--text-on-blue);
    flex: none;
  }
  .brand-text { color: var(--text-on-blue); }
  .brand-name {
    font-weight: 400;
    font-size: 40px;
    letter-spacing: 0.5px;
    line-height: 1;
  }
  .brand-tagline {
    font-weight: 400;
    font-size: 13px;
    letter-spacing: 5px;
    margin-top: 8px;
    text-transform: uppercase;
  }
  /* Back side */
  .card--back {
    top: 530px;
    background: var(--card-white);
    display: flex;
    align-items: center;
    padding: 0 40px 0 56px;
  }
  .back-brand {
    display: flex;
    flex-direction: column;
    align-items: center;
    gap: 12px;
    width: 150px;
    flex: none;
  }
  .back-brand .brand-dot {
    width: 78px;
    height: 78px;
    background: var(--brand-blue);
  }
  .back-brand-name {
    font-weight: 600;
    font-size: 16px;
    color: var(--brand-blue);
  }
  .divider {
    width: 1px;
    height: 110px;
    background: var(--divider);
    margin: 0 26px 0 22px;
    flex: none;
  }
  .person-name {
    font-size: 30px;
    line-height: 1;
    color: var(--brand-blue-deep);
    text-transform: uppercase;
  }
  .person-name .first { font-weight: 800; }
  .person-name .last { font-weight: 300; }
  .person-role {
    font-size: 11.5px;
    font-weight: 600;
    color: var(--ink-dark);
    text-transform: uppercase;
    letter-spacing: 0.6px;
    margin-top: 4px;
  }
  .qualifications {
    list-style: none;
    margin-top: 18px;
    font-size: 12.5px;
    font-weight: 600;
    line-height: 1.35;
    color: var(--brand-blue-deep);
    text-transform: uppercase;
    letter-spacing: 0.3px;
  }
</style>
</head>
<body>
  <main class="stage">
    <section class="card card--front" aria-label="Card front">
      <span class="brand-dot" aria-hidden="true"></span>
      <div class="brand-text">
        <h1 class="brand-name">Kindred Lane</h1>
        <p class="brand-tagline">Find Yourself</p>
      </div>
    </section>

    <section class="card card--back" aria-label="Card back">
      <div class="back-brand">
        <span class="brand-dot" aria-hidden="true"></span>
        <span class="back-brand-name">Kindred Lane</span>
      </div>
      <span class="divider" aria-hidden="true"></span>
      <div class="person">
        <h2 class="person-name"><span class="first">Derek</span> <span class="last">Hollis</span></h2>
        <p class="person-role">Counsellor &amp; Psychotherapist</p>
        <ul class="qualifications">
          <li>BSc (Psychol.),</li>
          <li>BA, Dip. (Couns. &amp; Psych.),</li>
          <li>PG.Cert (CBT), ADLnR, ESGW</li>
        </ul>
      </div>
    </section>
  </main>
</body>
</html>
```